Web Design Project

I want customers to be able to book appointments to get their makeup done and make a deposit and also have a gallery where i put my portfolio images, i want it to be very simple yet elegant.

Target Market(s)

Women ranging from 18-40 that want to get their makeup done

Industry/Entity Type

Makeup

Font styles to use
Sans Serif
Decorative

Requirements
Nice to have
• easy scheduling option and option to pay service in full on website.

```html
<!DOCTYPE html>
<html lang="en">
<head>
<meta charset="utf-8">
<title>Luma Makeup Studio</title>
<link rel="stylesheet" href="https://fonts.googleapis.com/css2?family=Arimo:ital,wght@0,400;0,700;1,400&display=swap">
<style>
  :root {
    --page: #ffffff;
    --rule: #c8c8c8;
    --ink: #111111;
    --coupon: #d9d9d9;
    --nav: #828282;
    --blog: #c696a9;
    --mauve: #867188;
    --sage: #8aa89f;
    --card: #ffffff;
    --light: #ffffff;
  }
  * { box-sizing: border-box; margin: 0; padding: 0; }
  html, body { width: 1200px; height: 537px; overflow: hidden; background: var(--page); }
  body { font-family: "Arimo", Arial, sans-serif; color: var(--ink); position: relative; border-top: 1px solid var(--rule); }

  .coupon { position: absolute; top: 40px; width: 249px; height: 103px; }
  .coupon--left { left: 193px; }
  .coupon--right { left: 764px; }
  .coupon svg { position: absolute; inset: 0; }
  .coupon__text { position: relative; padding: 16px 12px 0; text-align: center; font-size: 12.5px; line-height: 14.5px; }
  .coupon__title { font-weight: 700; }
  .coupon__note { font-style: italic; }

  .brand { position: absolute; left: 478px; top: 62px; width: 250px; text-align: center; }
  .brand__name { display: block; font-size: 50px; line-height: 56px; font-weight: 700; letter-spacing: 0; }
  .brand__tagline { display: block; font-size: 10px; line-height: 12px; letter-spacing: 0.6px; margin-top: 14px; }

  .nav { position: absolute; left: 165px; top: 173px; width: 872px; height: 31px; display: flex; background: var(--nav); }
  .nav__item { color: var(--light); font-size: 12.5px; line-height: 31px; text-align: center; text-decoration: none; position: relative; white-space: nowrap; }
  .nav__item--divided::after { content: ""; position: absolute; right: 0; top: 8px; width: 2px; height: 16px; background: var(--light); }
  .nav__item--blog { background: var(--blog); }
  .nav__item--book { background: var(--sage); }

  .services { position: absolute; left: 165px; top: 204px; width: 519px; height: 333px; background: var(--mauve); }
  .services__intro { color: var(--light); text-align: center; font-size: 14.2px; line-height: 20.5px; padding: 16px 40px 0; }
  .menu { position: absolute; left: 27px; top: 97px; width: 466px; height: 300px; background: var(--card); padding: 20px 36px 0; text-align: center; }
  .menu__item { margin-bottom: 20px; }
  .menu__title { font-size: 14.2px; line-height: 18px; font-weight: 400; }
  .menu__desc { font-size: 10px; line-height: 15px; }

  .studio { position: absolute; left: 684px; top: 204px; width: 353px; height: 333px; background: var(--sage); color: var(--light); text-align: center; font-size: 14.2px; line-height: 20.5px; padding: 16px 28px 0; }
  .studio p { margin-bottom: 20.5px; }
</style>
</head>
<body>
  <aside class="coupon coupon--left">
    <svg width="249" height="103" viewBox="0 0 249 103" aria-hidden="true">
      <path d="M13 0 H236 A13 13 0 0 0 249 13 V90 A13 13 0 0 0 236 103 H13 A13 13 0 0 0 0 90 V13 A13 13 0 0 0 13 0 Z" fill="var(--coupon)"/>
    </svg>
    <div class="coupon__text">
      <div class="coupon__title">JANUARY MONDAY SPECIAL:</div>
      <div>Get Free Faux Lashes when you book a gorgeous Lorem Ipsum look every Monday in January!</div>
      <div class="coupon__note">That's a $40 savings!</div>
    </div>
  </aside>

  <header class="brand">
    <span class="brand__name">LUMA</span>
    <span class="brand__tagline">AMAZING MAKEUP JUST FOR YOU</span>
  </header>

  <aside class="coupon coupon--right">
    <svg width="249" height="103" viewBox="0 0 249 103" aria-hidden="true">
      <path d="M13 0 H236 A13 13 0 0 0 249 13 V90 A13 13 0 0 0 236 103 H13 A13 13 0 0 0 0 90 V13 A13 13 0 0 0 13 0 Z" fill="var(--coupon)"/>
    </svg>
    <div class="coupon__text">
      <div class="coupon__title">JANUARY MONDAY SPECIAL:</div>
      <div>Get Free Faux Lashes when you book a gorgeous Lorem Ipsum look every Monday in January!</div>
      <div class="coupon__note">That's a $40 savings!</div>
    </div>
  </aside>

  <nav class="nav">
    <a class="nav__item nav__item--divided" style="width:144px" href="#">MAKEUP SERVICES</a>
    <a class="nav__item nav__item--divided" style="width:138px" href="#">WEDDING MAKEUP</a>
    <a class="nav__item nav__item--divided" style="width:165px" href="#">BACHELORETTE PARTY</a>
    <a class="nav__item nav__item--divided" style="width:103px" href="#">GALLERY</a>
    <a class="nav__item" style="width:112px" href="#">ABOUT US</a>
    <a class="nav__item nav__item--blog" style="width:87px" href="#">BLOG</a>
    <a class="nav__item nav__item--book" style="width:123px" href="#">BOOK NOW</a>
  </nav>

  <main class="services">
    <p class="services__intro">Lorem ipsum dolor sit amet, consectetur adipiscing elit, sed do eiusmod tempor incididunt ut labore et dolore magna aliqua. Ut enim ad minim veniam, quis nostru.</p>
    <section class="menu">
      <div class="menu__item">
        <h3 class="menu__title">$60 - Our Full Face Makeup Application</h3>
        <p class="menu__desc">Includes foundation, powder, blush, concealer, bronzer, eye shadow, eyeliner, brow fill-in, mascara and lip color. Excludes eye lash application and brow shaping. (45 mins)</p>
      </div>
      <div class="menu__item">
        <h3 class="menu__title">$40 - Our Quickie</h3>
        <p class="menu__desc">In a hurry? Don't worry - we can still satisfy you. We'll provide you with a simple but beautiful makeup application. Includes sheer coverage (tinted moisturizer), powder, blush, light concealer, lip color, brow fill-in &amp; mascara. Does not include eye makeup, lashes or eyebrows (all of which are additional time &amp; cost). Not suggested for problem skin and those who like more coverage. (approx 25 mins)</p>
      </div>
      <div class="menu__item">
        <h3 class="menu__title">$35 - For Your Eyes Only</h3>
      </div>
    </section>
  </main>

  <section class="studio">
    <p>Our beautifully designed studio is a wonderful place to sit back, relax &amp; enjoy the creation of your gorgeous look.</p>
    <p>Call us:&nbsp; 123-555-0142</p>
    <p>Or stop by:&nbsp; 123 Willow Lane</p>
    <p>We offer complimentary access to our spacious Dressing Room &amp; Shower every time you visit the studio. It's a great place for a little makeover: to change your clothes, fix your hair or just take a few minutes to prepare for what's next. The dressing room even has storage lockers if you'd like to leave some things behind and pick them up later (or have</p>
  </section>
</body>
</html>
```